Brand New Church Business Card Design. Needs to appeal to high school students, professionals.

Business Card. Bold lines and colors. Simple font. This is a new church looking to attract new families who have moved to the area. Business professionals mostly. have a working logo. may need a little tweaking. Church is designed to do excellent ministries for students and children. Like business card design in box on mark vault homepage. Want a front and back side. Prefer colors to match the logo. But will lean on designers preferences and wisdom. DO NOT WANT A CROSS OR RELIGIOUS SYMBOL on the card.

Target Market(s)

Families, Professionals, Students

Industry/Entity Type

High School

Contact Information for Business Card

SaltRock ChurchSaltRock.atForrest Coulter904-515-8349Forrest@PineHollow.at

Font styles to use
Sans Serif

Colors
0255a3
ffffff

Requirements
Must have
• Bold colors. Very Masculine. Creative
Nice to have
• On printnook.markvault.com homepage in the business card design box. the card with the black, blue and gray looks really sharp. matches our logos.
Should not have
• no crosses or religious symbols.

```html
<!DOCTYPE html>
<html lang="en">
<head>
<meta charset="utf-8">
<title>PineHollow Church – Business Card</title>
<link href="https://fonts.googleapis.com/css2?family=PT+Sans:wght@400;700&family=PT+Sans+Narrow:wght@700&display=swap" rel="stylesheet">
<style>
  :root {
    --backdrop: #6e0b0f;
    --paper: #ffffff;
    --navy: #0c1826;
    --teal: #04597c;
    --sky: #47a6dd;
    --ice: #87d0f3;
    --frost: #e4f3fc;
    --brand-blue: #0a6cb8;
    --brand-ink: #0d2b4b;
    --grey-text: #333a40;
  }
  * { margin: 0; padding: 0; box-sizing: border-box; }
  html, body { width: 1200px; height: 970px; overflow: hidden; }
  body {
    position: relative;
    background: var(--backdrop);
    font-family: "PT Sans", Arial, sans-serif;
  }
  .card {
    position: absolute;
    background: var(--paper);
    box-shadow: 0 6px 24px rgba(0,0,0,.45);
    overflow: hidden;
  }

  /* Front */
  .card--front { left: 60px; top: 42px; width: 720px; height: 445px; }
  .card--front .brand { position: absolute; left: 232px; top: 150px; }
  .card--front .site {
    position: absolute; left: 278px; top: 292px;
    font-size: 21px; color: var(--grey-text);
  }
  .swatch-band { position: absolute; left: 0; bottom: 0; width: 100%; height: 42px; display: flex; }
  .swatch-band span { height: 100%; }
  .swatch--navy { width: 404px; background: var(--navy); }
  .swatch--teal { width: 86px; background: var(--teal); }
  .swatch--sky { width: 86px; background: var(--sky); }
  .swatch--ice { width: 86px; background: var(--ice); }
  .swatch--frost { flex: 1; background: var(--frost); }

  /* Brand lockup */
  .brand { display: flex; align-items: center; gap: 16px; }
  .brand__dot { width: 72px; height: 72px; border-radius: 50%; background: var(--brand-blue); flex: none; }
  .brand__name {
    font-family: "PT Sans", Arial, sans-serif;
    font-weight: 700; font-size: 38px; line-height: 1.02;
    color: var(--brand-ink);
  }

  /* Back */
  .card--back { left: 403px; top: 512px; width: 772px; height: 440px; }
  .card--back .brand { position: absolute; left: 52px; top: 175px; }
  .contact-panel { position: absolute; left: 386px; top: 0; width: 386px; height: 100%; background: var(--frost); }
  .contact-panel__name {
    height: 146px; background: var(--navy);
    display: flex; align-items: center; justify-content: center;
    font-family: "PT Sans Narrow", "Arial Narrow", sans-serif;
    font-weight: 700; font-size: 48px; color: #fff;
  }
  .contact-row {
    height: 87px; margin-top: 2px;
    display: flex; align-items: center;
    padding-left: 14px; gap: 26px;
    font-size: 23px; letter-spacing: .5px;
  }
  .contact-row--phone { background: var(--teal); color: #fff; }
  .contact-row--email { background: var(--sky); color: #fff; }
  .contact-row--web { background: var(--ice); color: var(--navy); }
  .contact-row svg { width: 50px; height: 50px; flex: none; }
</style>
</head>
<body>

<section class="card card--front" aria-label="Card front">
  <div class="brand">
    <span class="brand__dot"></span>
    <span class="brand__name">PineHollow<br>Church</span>
  </div>
  <p class="site">www.PineHollow.at</p>
  <div class="swatch-band">
    <span class="swatch--navy"></span>
    <span class="swatch--teal"></span>
    <span class="swatch--sky"></span>
    <span class="swatch--ice"></span>
    <span class="swatch--frost"></span>
  </div>
</section>

<section class="card card--back" aria-label="Card back">
  <div class="brand">
    <span class="brand__dot"></span>
    <span class="brand__name">PineHollow<br>Church</span>
  </div>
  <div class="contact-panel">
    <h1 class="contact-panel__name">Dwayne Pellish</h1>
    <div class="contact-row contact-row--phone">
      <svg viewBox="0 0 50 50" aria-hidden="true">
        <circle cx="25" cy="25" r="23" fill="none" stroke="#fff" stroke-width="2"/>
        <path d="M20 15c-2 1-3 3-3 5 0 6 5 14 11 15 2 0 3-1 4-3l-3-3-2 1c-2-1-4-5-4-7l2-1-1-4z" fill="#fff"/>
      </svg>
      <span>904-555-0172</span>
    </div>
    <div class="contact-row contact-row--email">
      <svg viewBox="0 0 50 50" aria-hidden="true">
        <circle cx="25" cy="25" r="23" fill="none" stroke="#0c1826" stroke-width="2"/>
        <text x="25" y="33" text-anchor="middle" font-family="Arial, sans-serif" font-weight="700" font-size="26" fill="#0c1826">@</text>
      </svg>
      <span>Dwayne@PineHollow.at</span>
    </div>
    <div class="contact-row contact-row--web">
      <svg viewBox="0 0 50 50" aria-hidden="true">
        <circle cx="25" cy="25" r="23" fill="none" stroke="#0c1826" stroke-width="2"/>
        <g fill="none" stroke="#0c1826" stroke-width="1.6">
          <circle cx="25" cy="25" r="12"/>
          <ellipse cx="25" cy="25" rx="5.5" ry="12"/>
          <line x1="13" y1="25" x2="37" y2="25"/>
          <line x1="15" y1="19" x2="35" y2="19"/>
          <line x1="15" y1="31" x2="35" y2="31"/>
        </g>
      </svg>
      <span>www.PineHollow.at</span>
    </div>
  </div>
</section>

</body>
</html>
```